Moving Postcard

I need a postcard to let people know my law firm is moving effective Jan 1 2018 to Harlow Tower Suite 2700 2836 Larkmoor Street Seattle Washington 98127-3460. A copy of my current letterhead, business card, and envelope (all of which I like) are attached. The color is odd on the scan but it's a dark purple or purplish-brown. I was to keep the 'steady, resolute advocacy' (but drop the criminal) and perhaps specify elsewhere I'm talking about criminal defense, lawyer discipline defense, and judicial conduct defense. I'd like a design I can easily upload and have printed by Zint

Law Firm

```html
<!DOCTYPE html>
<html lang="en">
<head>
<meta charset="utf-8">
<title>Dana Whitlock – Moving Postcard</title>
<link rel="stylesheet" href="https://fonts.googleapis.com/css2?family=Bebas+Neue&family=Oswald:wght@300;400;500&family=Open+Sans:wght@400&family=PT+Serif&display=swap">
<style>
  :root {
    --plum: #2a1520;
    --plum-ink: #3b2230;
    --brick: #8a4a3a;
    --brick-dark: #4e2a24;
    --white: #ffffff;
    --panel-grey: #ebeceb;
    --body-grey: #555555;
    --label-grey: #444444;
    --backdrop: #2c2c2c;
  }
  * { box-sizing: border-box; margin: 0; padding: 0; }
  html, body { width: 960px; height: 1200px; overflow: hidden; }
  body { background: var(--backdrop); position: relative; font-family: "Open Sans", sans-serif; }

  .card { position: absolute; left: 134px; width: 694px; overflow: hidden; }
  .card--front { top: 50px; height: 534px; }
  .card--back { top: 617px; height: 533px; background: var(--white); }

  /* front */
  .portrait-area { position: absolute; inset: 0;
    background: radial-gradient(ellipse at 30% 55%, #a0614d 0%, var(--brick) 45%, var(--brick-dark) 100%); }
  .front-swoosh { position: absolute; left: 0; top: 0; width: 694px; height: 534px; }
  .brand-name { position: absolute; left: 0; width: 694px; top: 24px; text-align: center;
    font-family: "Oswald", sans-serif; font-weight: 500; font-size: 48px; letter-spacing: 1px;
    color: var(--white); line-height: 1; transform: translateX(-12px); }
  .tagline { position: absolute; left: 0; width: 694px; top: 78px; text-align: center;
    font-family: "PT Serif", serif; font-size: 27px; color: var(--white); transform: translateX(-12px); }
  .move-notice { position: absolute; right: 15px; top: 160px; text-align: right; color: var(--white);
    font-family: "Bebas Neue", sans-serif; line-height: 1; }
  .move-notice__lead { font-size: 48px; letter-spacing: -0.5px; }
  .move-notice__date { font-size: 70px; margin-top: 0; }
  .move-notice__date sup { font-size: 26px; vertical-align: 32px; }
  .new-address { position: absolute; right: 19px; top: 280px; text-align: right; color: var(--white);
    font-family: "Oswald", sans-serif; font-weight: 300; font-size: 21px; line-height: 27px; font-style: normal; }
  .new-address svg { width: 18px; height: 22px; vertical-align: -3px; margin-right: 8px; }
  .front-contact { position: absolute; right: 18px; top: 440px; text-align: right; color: var(--white); }
  .phone { font-family: "Bebas Neue", sans-serif; font-size: 52px; line-height: 1; }
  .email, .web { font-family: "Oswald", sans-serif; font-weight: 300; font-size: 22px; line-height: 28px; }
  .front-contact .email { font-size: 25px; line-height: 32px; }

  /* back */
  .about { position: absolute; left: 18px; top: 22px; width: 496px; text-align: justify;
    font-size: 12px; line-height: 16px; color: var(--body-grey); }
  .about p + p { margin-top: 16px; }
  .practice { position: absolute; left: 20px; top: 162px; color: var(--plum-ink); }
  .practice__intro { font-family: "Oswald", sans-serif; font-weight: 300; font-size: 22px; line-height: 28px; }
  .practice__list { font-family: "Bebas Neue", sans-serif; font-size: 32px; line-height: 27px; letter-spacing: -0.3px; margin-top: 2px; }
  .practice__list span { font-family: "Oswald", sans-serif; font-weight: 300; font-size: 22px; }
  .back-band { position: absolute; left: 0; top: 280px; width: 336px; height: 165px; }
  .back-contact { position: absolute; left: 46px; top: 332px; color: var(--white); }
  .back-contact .phone { font-size: 55px; }
  .back-contact .email, .back-contact .web { font-size: 23px; line-height: 27px; }

  .mail-zone { position: absolute; background: var(--panel-grey); display: flex; align-items: center;
    justify-content: center; text-align: center; font-size: 17px; line-height: 18px; color: var(--label-grey); }
  .mail-zone--postage { left: 526px; top: 10px; width: 160px; height: 158px; }
  .mail-zone--address { left: 336px; top: 168px; width: 350px; height: 277px; align-items: flex-start; padding-top: 54px; }
  .mail-zone--barcode { left: 0; top: 445px; width: 686px; height: 78px; }
</style>
</head>
<body>
  <section class="card card--front">
    <div class="portrait-area" role="img" aria-label="Portrait photo of the attorney in front of a red brick wall"></div>
    <svg class="front-swoosh" viewBox="0 0 694 534" aria-hidden="true">
      <path d="M0,372 C120,342 300,352 372,392 C470,450 600,430 694,368 L694,534 L0,534 Z" fill="var(--plum)"/>
      <path d="M0,366 C120,336 300,346 372,386 C470,444 600,424 694,362" fill="none" stroke="var(--white)" stroke-width="6"/>
    </svg>
    <h1 class="brand-name">DANA WHITLOCK</h1>
    <p class="tagline">steady, resolute advocacy</p>
    <div class="move-notice">
      <div class="move-notice__lead">WE ARE MOVING EFFECTIVE</div>
      <div class="move-notice__date">1<sup>ST</sup> JAN 2018</div>
    </div>
    <address class="new-address">
      <div><svg viewBox="0 0 18 22"><path d="M9 0C4 0 0 4 0 8.8 0 15 9 22 9 22s9-7 9-13.2C18 4 14 0 9 0z" fill="var(--white)"/><circle cx="9" cy="8.5" r="3.3" fill="var(--brick)"/></svg>Harlow Tower Suite 2700 2836 Larkmoor Street</div>
      <div>Seattle Washington 98127-3460</div>
    </address>
    <div class="front-contact">
      <div class="phone">206.555.0147</div>
      <div class="email">dana@harborcitydefense.com</div>
    </div>
  </section>

  <section class="card card--back">
    <div class="about">
      <p>Dana Whitlock is a fearless criminal defense attorney intensely devoted to advocating on behalf of individuals accused of committing serious crimes in Washington state. Ms. Whitlock has built an incredibly strong background in criminal trial and appellate practice and has been recognized repeatedly for her acumen in these areas.</p>
      <p>Ms. Whitlock’s practice also includes disciplinary inquiries directed towards judges, lawyers, and bar applicants, especially where such are based on criminal allegations or convictions.</p>
    </div>
    <div class="practice">
      <div class="practice__intro">We are talking about</div>
      <div class="practice__list">CRIMINAL DEFENSE,<br>LAWYER DISCIPLINE DEFENSE, <span>and</span><br>JUDICIAL CONDUCT DEFENSE.</div>
    </div>
    <svg class="back-band" viewBox="0 0 336 165" aria-hidden="true">
      <path d="M0,24 C80,0 150,6 210,26 C260,42 300,36 336,20 L336,165 L0,165 Z" fill="var(--plum)"/>
      <path d="M0,18 C80,-6 150,0 210,20 C260,36 300,30 336,14 L336,22 C300,38 260,44 210,28 C150,8 80,2 0,26 Z" fill="var(--white)"/>
    </svg>
    <div class="back-contact">
      <div class="phone">206.555.0147</div>
      <div class="email">dana@harborcitydefense.com</div>
      <div class="web">www.harborcitydefense.com</div>
    </div>
    <div class="mail-zone mail-zone--postage">Postage<br>Area</div>
    <div class="mail-zone mail-zone--address">Address Area</div>
    <div class="mail-zone mail-zone--barcode">Barcode Area</div>
  </section>
</body>
</html>
```